Inground sprinkler service and installation company requires a van wrap

The name of the company is Raincrest Irrigation. We have a new logo. We install sprinkler systems. We need a van wrap design using our new logo. We use Holvan 3400 extended vans. We are part of a group of companies and want to show that by having a blue banner along the top 8 inches that says 'part of the Verdaplex service group'. The design should identify that we do "service" "installation" "all makes" "design" "residential & commercial" "water conservation" Our current website has the OLD logo and is being revamped but is www.raincrestirrigation-example.com. My preference is clean and simple.

```html
<!DOCTYPE html>
<html lang="en">
<head>
<meta charset="utf-8">
<title>Raincrest Irrigation – Van Wrap Side Panels</title>
<link href="https://fonts.googleapis.com/css2?family=Ubuntu:wght@400;500;700&family=Roboto+Condensed:wght@700&display=swap" rel="stylesheet">
<style>
  :root {
    --wrap-blue: #1e9fd6;
    --wrap-blue-deep: #1479b8;
    --wrap-green: #24a94b;
    --wrap-white: #ffffff;
    --page-bg: #f2f3f5;
    --panel-edge: #d9dde2;
  }
  * { margin: 0; padding: 0; box-sizing: border-box; }
  html, body {
    width: 1200px; height: 1200px; overflow: hidden;
    background: var(--page-bg);
  }
  .wrap-sheet { position: relative; width: 1200px; height: 1200px; }
  .side-panel {
    position: absolute; left: 50px; width: 1100px; height: 320px;
    border-radius: 14px; overflow: hidden;
    box-shadow: 0 0 0 1px var(--panel-edge);
  }
  .side-panel--driver { top: 170px; }
  .side-panel--passenger { top: 650px; }
  .side-panel svg { display: block; }
  .fill-blue { fill: var(--wrap-blue); }
  .fill-blue-deep { fill: var(--wrap-blue-deep); }
  .fill-white { fill: var(--wrap-white); }
  .stroke-green { stroke: var(--wrap-green); fill: none; }
  .segment-label {
    font-family: "Roboto Condensed", "Ubuntu", sans-serif; font-weight: 700;
    font-size: 25px; fill: var(--wrap-white); letter-spacing: 0.3px;
  }
  .feature-label {
    font-family: "Ubuntu", sans-serif; font-weight: 500;
    font-size: 16px; fill: var(--wrap-white);
  }
  .brand-name {
    font-family: "Ubuntu", sans-serif; font-weight: 500;
    font-size: 54px; fill: var(--wrap-green); letter-spacing: 3px;
  }
  .brand-sub {
    font-family: "Ubuntu", sans-serif; font-weight: 500;
    font-size: 21px; fill: var(--wrap-green); letter-spacing: 6px;
  }
  .phone-number {
    font-family: "Ubuntu", sans-serif; font-weight: 700;
    font-size: 26px; fill: var(--wrap-blue);
  }
  .web-address {
    font-family: "Ubuntu", sans-serif; font-weight: 700;
    font-size: 11px; fill: var(--wrap-blue);
  }
  .service-line {
    font-family: "Ubuntu", sans-serif; font-weight: 500;
    font-size: 22px; fill: var(--wrap-white);
  }
  .group-banner-text {
    font-family: "Ubuntu", sans-serif; font-weight: 700;
    font-size: 12px; fill: var(--wrap-white); letter-spacing: 2px;
  }
</style>
</head>
<body>
<main class="wrap-sheet">

  <!-- Driver side: rear of van on the left -->
  <section class="side-panel side-panel--driver" aria-label="Driver side wrap panel">
    <svg width="1100" height="320" viewBox="0 0 1100 320">
      <defs>
        <linearGradient id="productFadeA" x1="0" y1="0" x2="1" y2="1">
          <stop offset="0" stop-color="#6cc3e8" stop-opacity="0.55"/>
          <stop offset="1" stop-color="#1e9fd6" stop-opacity="0"/>
        </linearGradient>
      </defs>
      <rect class="fill-white" width="1100" height="320"/>
      <polygon class="fill-blue" points="0,0 215,0 318,232 1100,232 1100,320 0,320"/>
      <rect x="18" y="160" width="150" height="110" fill="url(#productFadeA)"
            role="img" aria-label="Faded photo of a sprinkler head in grass"/>
      <path class="stroke-green" stroke-width="11" d="M238 -4 L336 218 L1100 218"/>

      <rect class="fill-blue-deep" x="0" y="0" width="1100" height="26"/>
      <text class="group-banner-text" x="680" y="18" text-anchor="middle">PART OF THE VERDAPLEX SERVICE GROUP</text>

      <text class="segment-label" x="30" y="72">RESIDENTIAL</text>
      <text class="segment-label" x="30" y="100">COMMERCIAL</text>
      <text class="feature-label" x="30" y="140">Water Conservation</text>

      <text class="brand-name" x="560" y="128" text-anchor="middle">RAINCREST</text>
      <text class="brand-sub" x="560" y="160" text-anchor="middle">IRRIGATION</text>

      <text class="phone-number" x="760" y="178">613-555-0142</text>
      <text class="web-address" x="760" y="196">www.raincrestirrigation-example.com</text>

      <text class="service-line" x="660" y="285" text-anchor="middle">Service - Installation - Design - All Makes</text>
    </svg>
  </section>

  <!-- Passenger side: rear of van on the right -->
  <section class="side-panel side-panel--passenger" aria-label="Passenger side wrap panel">
    <svg width="1100" height="320" viewBox="0 0 1100 320">
      <defs>
        <linearGradient id="productFadeB" x1="1" y1="0" x2="0" y2="1">
          <stop offset="0" stop-color="#6cc3e8" stop-opacity="0.55"/>
          <stop offset="1" stop-color="#1e9fd6" stop-opacity="0"/>
        </linearGradient>
      </defs>
      <rect class="fill-white" width="1100" height="320"/>
      <polygon class="fill-blue" points="1100,0 885,0 782,232 0,232 0,320 1100,320"/>
      <rect x="932" y="160" width="150" height="110" fill="url(#productFadeB)"
            role="img" aria-label="Faded photo of a sprinkler head in grass"/>
      <path class="stroke-green" stroke-width="11" d="M862 -4 L764 218 L0 218"/>

      <rect class="fill-blue-deep" x="0" y="0" width="1100" height="26"/>
      <text class="group-banner-text" x="420" y="18" text-anchor="middle">PART OF THE VERDAPLEX SERVICE GROUP</text>

      <text class="segment-label" x="1070" y="72" text-anchor="end">RESIDENTIAL</text>
      <text class="segment-label" x="1070" y="100" text-anchor="end">COMMERCIAL</text>
      <text class="feature-label" x="1070" y="140" text-anchor="end">Water Conservation</text>

      <text class="brand-name" x="560" y="128" text-anchor="middle">RAINCREST</text>
      <text class="brand-sub" x="560" y="160" text-anchor="middle">IRRIGATION</text>

      <text class="phone-number" x="185" y="178">613-555-0142</text>
      <text class="web-address" x="185" y="196">www.raincrestirrigation-example.com</text>

      <text class="service-line" x="440" y="285" text-anchor="middle">Service - Installation - Design - All Makes</text>
    </svg>
  </section>

</main>
</body>
</html>
```